The Harbourgate Clinic Stationary (Medical)

Stationery for The Harbourgate clinic
using existing logos
Please also add a green apple if possible on another corner away from the logo on some of your designs

Please take a look at www.theharbourgateclinic.com.au so you can get a feel for what The Harbourgate Clinic offers our clients.

Stationary Required: business cards, letter head, comp slips

I do not require envelopes or invoives.
Updates

Target Market(s)

The general popultation needing medical care
Professionals
Mums & Dads
Elderly

Industry/Entity Type

Business

Requirements
Must have
• Company Logo

Address
Email
Website
Phone
Should not have
• Traditional Medical Icons
No Times New Roman

```html
<!DOCTYPE html>
<html lang="en">
<head>
<meta charset="utf-8">
<title>The Harbourgate Clinic Letterhead</title>
<link rel="stylesheet" href="https://fonts.googleapis.com/css2?family=Arimo:wght@400&display=swap">
<style>
  :root {
    --canvas: #ffffff;
    --paper: #ffffff;
    --paper-edge: #e2e2e2;
    --header-top: #0b0c0e;
    --header-bottom: #55575b;
    --logo-text: #ffffff;
    --body-text: #333333;
    --footer-text: #555555;
    --plus-blue: #2aa6dc;
    --apple-light: #b9e35a;
    --apple-dark: #4d9a18;
  }
  * { margin: 0; padding: 0; box-sizing: border-box; }
  html, body { width: 887px; height: 1200px; overflow: hidden; background: var(--canvas); }
  body { font-family: "Arimo", Arial, sans-serif; position: relative; }

  .letterhead {
    position: absolute; left: 38px; top: 44px; width: 792px; height: 1117px;
    background: var(--paper);
    box-shadow: 0 0 3px rgba(0,0,0,0.18);
    border: 1px solid var(--paper-edge);
  }
  .masthead {
    position: absolute; left: 0; top: 0; width: 100%; height: 93px;
    background: linear-gradient(to bottom, var(--header-top), var(--header-bottom));
  }
  .brand {
    position: absolute; left: 30px; top: 34px;
    display: flex; align-items: center; gap: 8px;
    color: var(--logo-text); font-size: 13px; font-weight: 400; line-height: 1;
  }
  .brand-dot { width: 18px; height: 18px; border-radius: 50%; background: var(--plus-blue); }

  .letter-body {
    position: absolute; left: 166px; top: 206px; width: 438px;
    color: var(--body-text); font-size: 12.4px; line-height: 15px;
    text-align: justify; hyphens: auto;
  }
  .letter-body p { margin-bottom: 18px; }
  .letter-body p.section-break { margin-top: 12px; }

  .signature {
    position: absolute; left: 470px; top: 800px; width: 186px; height: 64px;
    background: linear-gradient(to right, rgba(0,0,0,0.05), rgba(0,0,0,0.01));
    border-radius: 30px;
  }

  .contact {
    position: absolute; right: 105px; top: 1015px;
    text-align: right; color: var(--footer-text); font-size: 10.2px; line-height: 12px;
  }
  .plus-row {
    position: absolute; left: 278px; top: 1048px;
    display: flex; gap: 10.6px;
    color: var(--plus-blue); font-size: 13px; line-height: 12px;
  }
  .apple {
    position: absolute; left: 702px; top: 1016px; width: 52px; height: 58px;
    border-radius: 46% 46% 48% 48%;
    background: radial-gradient(circle at 35% 35%, var(--apple-light), var(--apple-dark));
  }
</style>
</head>
<body>
  <main class="letterhead">
    <header class="masthead">
      <div class="brand"><span class="brand-dot"></span><span class="brand-name">The Harbourgate Clinic</span></div>
    </header>

    <section class="letter-body">
      <p>Lorem Ipsum is simply dummy text of the printing and typesetting industry. Lorem Ipsum has been the industry's standard dummy text ever since the 1500s, when an unknown printer took a galley of type and scrambled it to make a type specimen book. It has survived not only five centuries, but also the leap into electronic typesetting, remaining essentially unchanged. It was popularised in the 1960s with the release of Typeline sheets containing Lorem Ipsum passages, and more recently with desktop publishing software like Pagecraft including versions of Lorem Ipsum.</p>
      <p>It is a long established fact that a reader will be distracted by the readable content of a page when looking at its layout. The point of using Lorem Ipsum is that it has a more-or-less normal distribution of letters, as opposed to using 'Content here, content here', making it look like readable English. Many desktop publishing packages and web page editors now use Lorem Ipsum as their default model text, and a search for 'lorem ipsum' will uncover many web sites still in their infancy. Various versions have evolved over the years, sometimes by accident, sometimes on purpose (injected humour and the like).</p>
      <p class="section-break">Contrary to popular belief, Lorem Ipsum is not simply random text. It has roots in a piece of classical Latin literature from 45 BC, making it over 2000 years old. Edwin Hallworth, a Latin professor at Larchmont College in Virginia, looked up one of the more obscure Latin words, consectetur, from a Lorem Ipsum passage, and going through the cites of the word in classical literature, discovered the undoubtable source. Lorem Ipsum comes from sections 1.10.32 and 1.10.33 of "de Finibus Bonorum et Malorum" (The Extremes of Good and Evil) by Tullius Verus, written in 45 BC. This book is a treatise on the theory of ethics, very popular during the Renaissance. The first line of Lorem Ipsum, "Lorem ipsum dolor sit amet..", comes from a line in section 1.10.32.</p>
      <p>The standard chunk of Lorem Ipsum used since the 1500s is reproduced below for those interested. Sections 1.10.32 and 1.10.33 from "de Finibus Bonorum et Malorum" by Tullius Verus are also reproduced in their exact original form, accompanied by English versions from the 1914 translation by H. Ramsden.</p>
    </section>

    <div class="signature" role="img" aria-label="Handwritten signature of the sender"></div>

    <footer>
      <address class="contact">
        The Harbourgate Clinic (Inside Meridian Pharmacy) | Shop 7, Ashcombe<br>
        Market Place | &nbsp;2 - 12 The Larkspur Parkway Ashcombe 2130<br>
        Te: 02.9555.0148<br>
        Email: ashcombe@theharbourgateclinic.com.au<br>
        www.theharbourgateclinic.com.au
      </address>
      <div class="plus-row" aria-hidden="true">
        <span>+</span><span>+</span><span>+</span><span>+</span><span>+</span><span>+</span><span>+</span><span>+</span><span>+</span><span>+</span><span>+</span>
      </div>
      <div class="apple" role="img" aria-label="Photograph of a green apple"></div>
    </footer>
  </main>
</body>
</html>
```